A Billboard Sign - TWO SIGNS

Hi, I’m looking to produce approximately 2.74 m by 2.74 m for a billboard-style display. I have a mock-up of the general look and feel, but I need a more polished, professional design. The sign will be viewed by people driving past, so the messaging must be clear, bold and easily readable at speed.

I also need a second sign sized 1 m by 3 m, following the same branding and visual style as the larger piece.

Requirements
Must have
• It must use the colours I've submitted
Nice to have
• I would like to see some good ideas in the general theme of what I have Mocked up. I don't the same design sent back to me

```html
<!DOCTYPE html>
<html lang="en">
<head>
<meta charset="utf-8">
<title>Luminant Systems – Billboard Signs</title>
<link rel="stylesheet" href="https://fonts.googleapis.com/css2?family=Montserrat:wght@600;700;800&display=swap">
<style>
  :root {
    --orange: #fca323;
    --ink: #1c1c1c;
    --band-square: #1f1f1f;
    --band-wide: #000000;
    --white: #ffffff;
    --partner-red: #e8251f;
    --partner-grey: #c9c9c9;
  }
  * { margin: 0; padding: 0; box-sizing: border-box; }
  html, body {
    width: 1200px; height: 471px; overflow: hidden;
    background: var(--white);
    font-family: "Montserrat", Arial, sans-serif;
  }
  .canvas { position: relative; width: 1200px; height: 471px; }

  .sign { position: absolute; top: 73px; background: var(--orange); overflow: hidden; }
  .sign--square { left: 93px; width: 324px; height: 324px; }
  .sign--wide { left: 469px; width: 651px; height: 325px; }

  .brand { position: absolute; display: flex; align-items: center; color: var(--ink); }
  .brand__dot { border-radius: 50%; background: var(--ink); flex: none; }
  .brand__name { font-weight: 800; text-transform: uppercase; line-height: 1.08; letter-spacing: 0.02em; }

  .sign--square .brand { left: 36px; top: 50px; }
  .sign--square .brand__dot { width: 72px; height: 72px; margin-right: 16px; }
  .sign--square .brand__name { font-size: 25px; }

  .sign--wide .brand { left: 102px; top: 33px; }
  .sign--wide .brand__dot { width: 124px; height: 124px; margin-right: 28px; }
  .sign--wide .brand__name { font-size: 43px; }

  .tagline {
    position: absolute; left: 0; right: 0; text-align: center;
    font-weight: 800; color: var(--ink); text-transform: uppercase; line-height: 1.05;
  }
  .sign--square .tagline { top: 140px; font-size: 14px; }
  .sign--wide .tagline { top: 183px; font-size: 14.5px; letter-spacing: 0.01em; }

  .award { position: absolute; }
  .sign--square .award { left: 129px; top: 181px; width: 66px; height: 66px; }
  .sign--wide .award { left: 295px; top: 209px; width: 58px; height: 58px; }

  .web { position: absolute; font-weight: 700; }
  .sign--square .web { right: 15px; top: 291px; font-size: 9px; color: var(--ink); }
  .sign--wide .web { left: 24px; top: 296px; font-size: 12.5px; color: var(--white); }

  .band { position: absolute; left: 0; right: 0; bottom: 0; }
  .sign--square .band { height: 39px; background: var(--band-square); }
  .sign--wide .band { height: 40px; background: var(--band-wide); }

  .partners { position: absolute; display: flex; align-items: center; }
  .sign--square .partners { left: 16px; top: 13px; }
  .sign--wide .partners { left: 356px; top: 13px; }
  .partners__label { font-size: 4.5px; font-weight: 700; color: var(--white); text-transform: uppercase; letter-spacing: 0.03em; margin-right: 22px; }
  .sign--wide .partners__label { margin-right: 22px; }
  .partner { font-weight: 700; font-size: 12.5px; line-height: 1; display: flex; align-items: center; }
  .partner--norvale { color: var(--partner-red); letter-spacing: 0.05em; margin-right: 20px; }
  .partner--kestrel { color: var(--partner-grey); font-weight: 600; }
  .partner--kestrel .partner__mark { width: 15px; height: 15px; background: var(--partner-grey); margin-right: 4px; }
</style>
</head>
<body>
<main class="canvas">

  <section class="sign sign--square">
    <div class="brand">
      <span class="brand__dot"></span>
      <span class="brand__name">Luminant<br>Systems</span>
    </div>
    <p class="tagline">Award winning data analytics<br>implementation partner</p>
    <svg class="award" viewBox="0 0 66 66" aria-hidden="true">
      <circle cx="33" cy="33" r="30" fill="var(--ink)"/>
      <path d="M20 33 L29 42 L47 24" fill="none" stroke="var(--orange)" stroke-width="6" stroke-linecap="round" stroke-linejoin="round"/>
    </svg>
    <p class="web">www.luminantsystems.ie</p>
    <div class="band">
      <div class="partners">
        <span class="partners__label">Proudly partnering with</span>
        <span class="partner partner--norvale">NORVALE</span>
        <span class="partner partner--kestrel"><span class="partner__mark"></span>Kestrelsoft</span>
      </div>
    </div>
  </section>

  <section class="sign sign--wide">
    <div class="brand">
      <span class="brand__dot"></span>
      <span class="brand__name">Luminant<br>Systems</span>
    </div>
    <p class="tagline">Award winning data analytics implementation partner</p>
    <svg class="award" viewBox="0 0 66 66" aria-hidden="true">
      <circle cx="33" cy="33" r="30" fill="var(--ink)"/>
      <path d="M20 33 L29 42 L47 24" fill="none" stroke="var(--orange)" stroke-width="6" stroke-linecap="round" stroke-linejoin="round"/>
    </svg>
    <div class="band">
      <p class="web">www.luminantsystems.ie</p>
      <div class="partners">
        <span class="partners__label">Proudly partnering with</span>
        <span class="partner partner--norvale">NORVALE</span>
        <span class="partner partner--kestrel"><span class="partner__mark"></span>Kestrelsoft</span>
      </div>
    </div>
  </section>

</main>
</body>
</html>
```